Digital Marketing Online Shop Needs a Home Page Web Design

Here is some background on the new home page and the message we want to relay to people visiting our site.
The new site design will be very similar to the following sites
http://trellisoft.com/
https://quillhaven.com/
http://brightmarrow.io/
http://sketchotter.com/
http://clipharbor.com/
We are a small marketing agency of 3 and we have built up and impressive contact list of partners over the last 16 years to help our customers take their digital marketing to the next level.
The four core areas of products we will be promoting and selling through our online shop are the following :
Web design
Content marketing
Graphic design
Coaching
We operate our agency in a new way, not the old school way so our customers can receive on-demand marketing.
We plan to have an online shop so visitors can purchase some of our services, very similar to how Quill Haven and Sketch Otter offer their services.
In the end, we want the same call to action layout as Trellisoft, Quill Haven and Sketch Otter, however, since we are an agency we would like to blend in Bright Marrow's layout.
We want the customer to either contact us about our services or purchase one of the services from our shop.
We are trying to make the whole digital marketing experience more transactional like retail and not so traditional servicey. :-)
It is from our years of experience and finding the right partners that allows us to offer this type of solution to businesses in the Maritime Provinces (New Brunswick, Nova Scotia, Prince Edward Island, Canada).
Also, because we are offering more of an on-demand/self serve option and we have lower overhead, we hope to pass along great pricing to our customers for their marketing needs. We really want this offer to expand outside of our local market in Saint John, New Brunswick.
I would also like to have a call to action written for a hero image at the top of the page, like the Trellisoft site.
After that I would like the content to flow through similar to Quill Haven & Trellisoft. But mix in some of the agency like content you see with Clipharbor, Bright Marrow.
I have also included the first draft of the content for our home page.
Menu Items will be About, How We Work, Learn, Shop, Contact
Please let me know if you need anything else.
Target Market(s)
Small businesses, 1-10 person companies with up to 5 million in revenue. Mostly service companies, but some retail.
Industry/Entity Type
Marketing
Number of Pages Required
1 page

```html
<!DOCTYPE html>
<html lang="en">
<head>
<meta charset="utf-8">
<title>Harbourline Studio — Home</title>
<link rel="stylesheet" href="https://fonts.googleapis.com/css2?family=Roboto:wght@300;400;500;700&display=swap">
<style>
:root{
  --blue:#2b6cc4;
  --blue-dark:#1f4f93;
  --ink:#222a33;
  --body:#5d6670;
  --muted:#8a939c;
  --line:#dfe3e8;
  --grey-band:#f2f3f5;
  --footer:#eceef1;
  --bottom:#23262b;
  --purple:#7a4fe3;
  --green:#5cc26a;
  --cyan:#0db6ee;
  --white:#ffffff;
}
*{margin:0;padding:0;box-sizing:border-box}
html,body{width:1200px;height:3681px;overflow:hidden}
body{font-family:"Roboto",Arial,sans-serif;color:var(--ink);background:var(--white);position:relative}
.abs{position:absolute}
section,header,footer{position:absolute;left:0;width:1200px}

/* header */
.site-header{top:0;height:82px;background:var(--white);border-bottom:1px solid var(--line)}
.brand{left:86px;top:22px;display:flex;align-items:center;gap:10px}
.brand-dot{width:34px;height:34px;border-radius:50%;background:var(--blue)}
.brand-name{font-size:22px;font-weight:500;color:var(--blue)}
.nav a{position:absolute;top:33px;font-size:14px;font-weight:500;color:var(--ink);text-decoration:none;letter-spacing:.3px}
.nav .active::after{content:"";position:absolute;left:-6px;right:-6px;top:47px;height:3px;background:var(--blue)}
.caret{display:inline-block;margin-left:8px;border:4px solid transparent;border-top-color:var(--ink);vertical-align:middle}

/* hero */
.hero{top:82px;height:585px;background:linear-gradient(180deg,#6a7584 0%,#555f6c 60%,#47505c 100%)}
.hero-art{position:absolute;inset:0;background:linear-gradient(120deg,rgba(240,130,60,.25),rgba(60,150,110,.25) 50%,rgba(50,90,160,.25))}
.hero h1{position:absolute;top:220px;width:100%;text-align:center;color:var(--white);font-size:42px;font-weight:500;letter-spacing:.5px}
.hero p{position:absolute;top:280px;left:220px;width:760px;text-align:center;color:var(--white);font-size:15px;line-height:24px}
.btn-ghost-light{position:absolute;top:340px;left:533px;width:134px;height:42px;border:2px solid var(--white);border-radius:21px;color:var(--white);font-size:13px;font-weight:700;text-align:center;line-height:38px}
.hero-arrows{position:absolute;top:522px;left:565px}

/* shared headings */
.kicker{position:absolute;width:100%;text-align:center;font-size:13px;color:var(--blue);letter-spacing:.6px}
.title{position:absolute;width:100%;text-align:center;font-size:24px;font-weight:500;color:var(--ink)}
.title-rule{position:absolute;left:570px;width:60px;height:2px;background:var(--blue)}
.btn-outline{position:absolute;height:40px;border:2px solid var(--blue);border-radius:20px;color:var(--blue);font-size:12px;font-weight:500;text-align:center;line-height:36px;background:var(--white)}

/* about */
.about{top:667px;height:437px}
.about .kicker-left{position:absolute;left:86px;top:67px;font-size:13px;color:var(--blue)}
.about h2{position:absolute;left:86px;top:92px;font-size:24px;font-weight:500}
.about .rule{position:absolute;left:86px;top:126px;width:60px;height:2px;background:var(--blue)}
.about-copy{position:absolute;left:86px;top:143px;width:630px;font-size:13.5px;line-height:1.55;color:var(--body);text-align:justify}
.about-copy p+p{margin-top:10px}
.about-photo{position:absolute;left:760px;top:70px;width:357px;height:288px;background:linear-gradient(135deg,#e9ecef,#cfd5db 60%,#b9a3a0);box-shadow:0 4px 14px rgba(0,0,0,.25)}

/* products */
.products{top:1104px;height:555px;background:var(--grey-band)}
.product{position:absolute;top:172px;width:230px;text-align:center}
.product-icon{width:108px;height:108px;border-radius:50%;margin:0 auto}
.product h3{margin-top:52px;font-size:17px;font-weight:500}
.product p{margin-top:8px;font-size:12px;line-height:1.5;color:var(--body);padding:0 10px}
.product .btn-outline{position:relative;display:inline-block;width:126px;height:34px;line-height:30px;font-size:11px;margin-top:14px}

/* pricing */
.pricing{top:1659px;height:579px}
.plan{position:absolute;top:172px;width:326px;height:329px;color:var(--white);text-align:center;overflow:hidden}
.plan-name{margin-top:45px;font-size:16px;font-weight:500}
.plan-price{font-size:52px;font-weight:500;line-height:1.1}
.plan-cur{font-size:15px}
.plan svg{position:absolute;left:0;bottom:0}

/* testimonials */
.testimonials{top:2238px;height:425px;background:linear-gradient(100deg,#2a2d33,#3b3f46 50%,#2c2f35)}
.testimonials .title{color:var(--white);top:80px}
.testimonials .kicker{top:58px;color:#9fb7d8}
.quote{position:absolute;top:140px;left:250px;width:700px;text-align:center;color:#e6e8ea;font-size:13px;line-height:1.6}
.avatar{position:absolute;top:2450px;left:554px;width:92px;height:92px;border-radius:50%}
.t-arrow{position:absolute;top:248px}
.client-name{position:absolute;top:318px;width:100%;text-align:center;color:var(--white);font-size:13px;font-weight:700}
.client-role{position:absolute;top:340px;width:100%;text-align:center;color:#c7cbd0;font-size:12px}

/* news */
.news{top:2663px;height:657px}
.post{position:absolute;top:174px;width:326px}
.post-image{position:relative;width:326px;height:218px;box-shadow:0 3px 10px rgba(0,0,0,.2)}
.post-date{position:absolute;left:0;right:0;bottom:0;height:36px;background:rgba(43,108,196,.55);color:var(--white);font-size:17px;font-weight:500;text-align:center;line-height:36px}
.post h3{margin-top:18px;font-size:17px;font-weight:500;line-height:1.2;width:230px}
.post p{margin-top:10px;font-size:12.5px;line-height:1.4;color:var(--body);width:280px}
.post .btn-outline{position:relative;display:inline-block;width:100px;height:34px;line-height:30px;font-size:11px;margin-top:14px}

/* footer */
.site-footer{top:3320px;height:300px;background:var(--footer)}
.f-col{position:absolute;top:46px}
.f-col h4{font-size:16px;font-weight:500;margin-bottom:22px}
.f-item{display:flex;align-items:flex-start;gap:16px;margin-bottom:14px;font-size:12px;color:var(--body);line-height:1.5}
.f-icon{flex:none;width:38px;height:38px;border-radius:50%;border:1.5px solid var(--blue);display:flex;align-items:center;justify-content:center}
.f-item b{display:block;color:var(--blue);font-weight:500;font-size:13px}
.f-links a{display:block;font-size:12px;color:var(--ink);text-decoration:underline;margin-bottom:12px}
.f-links a::before{content:"›";color:var(--blue);margin-right:10px;font-weight:700;text-decoration:none;display:inline-block}
.field{width:268px;height:38px;border-radius:19px;background:#e0e3e7;border:1px solid #d3d7dc;font-size:12px;color:var(--muted);padding-left:20px;line-height:36px}
.btn-solid{margin-top:14px;width:96px;height:36px;border-radius:18px;background:var(--blue);color:var(--white);font-size:12px;font-weight:700;text-align:center;line-height:36px}
.bottom-bar{top:3620px;height:61px;background:var(--bottom)}
.socials{position:absolute;left:86px;top:16px;display:flex;gap:10px}
.social{width:28px;height:28px;border-radius:50%;border:1.5px solid #c9ccd0}
.copyright{position:absolute;right:86px;top:22px;color:#d5d8dc;font-size:12px}
</style>
</head>
<body>

<header class="site-header">
  <div class="brand abs"><span class="brand-dot"></span><span class="brand-name">harbourline studio</span></div>
  <nav class="nav">
    <a href="#" class="active" style="left:421px">HOME</a>
    <a href="#" style="left:527px">ABOUT</a>
    <a href="#" style="left:640px">HOW WE WORK<span class="caret"></span></a>
    <a href="#" style="left:829px">LEARN</a>
    <a href="#" style="left:942px">SHOP</a>
    <a href="#" style="left:1045px">CONTACT</a>
  </nav>
</header>

<section class="hero">
  <div class="hero-art" role="img" aria-label="Illustration of a marketing team working together around a table"></div>
  <h1>WELCOME TO HARBOURLINE STUDIO</h1>
  <p>We are a small marketing agency of 3 and we have built up and impressive contact list ofpartners over<br>the last 16 years to help our customers take their digital marketing to thenext level.</p>
  <div class="btn-ghost-light">LEARN MORE</div>
  <svg class="hero-arrows" width="70" height="20" viewBox="0 0 70 20" fill="none" stroke="#fff" stroke-width="2"><path d="M10 4 4 10 10 16M16 4 10 10 16 16M54 4 60 10 54 16M60 4 66 10 60 16"/></svg>
</section>

<section class="about">
  <div class="kicker-left">Who we are</div>
  <h2>ABOUT US</h2>
  <div class="rule"></div>
  <div class="about-copy">
    <p>We are a small marketing agency of 3 and we have built up and impressive contact list ofpartners over the last 16 years to help our customers take their digital marketing to thenext level.We operate our agency in a new way, not the old school way so our customers canreceive on-demand marketing.</p>
    <p>We plan to have an online shop so visitors can purchase some of our services, verysimilar to how Quill Haven and Sketch Otter offer their services.In the end, we want the same call to action layout as Trellisoft, Quill Haven and Sketch Otter, however, since we are an agency we would like to blend in Bright Marrow's layout.</p>
  </div>
  <div class="btn-outline" style="left:86px;top:325px;width:116px">READ MORE</div>
  <div class="about-photo" role="img" aria-label="Photo of a presenter in a bright office beside a display stand"></div>
</section>

<section class="products">
  <div class="kicker" style="top:74px">What We will Give You</div>
  <div class="title" style="top:98px">OUR PRODUCTS</div>
  <div class="title-rule" style="top:134px"></div>

  <div class="product" style="left:93px">
    <div class="product-icon" role="img" aria-label="Web design icon" style="background:#4fb96a"></div>
    <h3>WEB DESIGN</h3>
    <p>Let's be honest. Your website is the face of your business in the modern-world. When done well, it can commu high-quality of service &gt;&gt;</p>
    <div class="btn-outline">PURCHASE NOW</div>
  </div>
  <div class="product" style="left:351px">
    <div class="product-icon" role="img" aria-label="Content marketing icon" style="background:#4d86e8"></div>
    <h3>CONTENT MARKETING</h3>
    <p>Content Marketing is to the 21 st century what traditional advertisingwas to the '60s. Thanks to the power of the internet &gt;&gt;</p>
    <div class="btn-outline">PURCHASE NOW</div>
  </div>
  <div class="product" style="left:616px">
    <div class="product-icon" role="img" aria-label="Graphic design icon" style="background:#56c4b8"></div>
    <h3>GRAPHIC DESIGN</h3>
    <p>Creating a consistent and eye-catching brand for your business is one of the best ways to draw in customers on the web. &gt;&gt;</p>
    <div class="btn-outline">PURCHASE NOW</div>
  </div>
  <div class="product" style="left:879px">
    <div class="product-icon" role="img" aria-label="Coaching icon" style="background:#f2c94c"></div>
    <h3>COACHING</h3>
    <p>Taking your small business to the next level can be a tricky process-Marketing jargon, of resources can make expanding &gt;&gt;</p>
    <div class="btn-outline">PURCHASE NOW</div>
  </div>
</section>

<section class="pricing">
  <div class="kicker" style="top:70px">Dont miss your chance</div>
  <div class="title" style="top:94px">PRICING TABLE</div>
  <div class="title-rule" style="top:130px"></div>

  <div class="plan" style="left:86px;background:var(--purple)">
    <div class="plan-name">BASIC</div><div class="plan-price">150</div><div class="plan-cur">USD</div>
    <svg width="326" height="150" viewBox="0 0 326 150"><polygon points="0,150 0,120 40,100 80,110 120,70 160,60 200,80 240,40 280,30 326,10 326,150" fill="rgba(255,255,255,.08)"/><polyline points="0,120 40,100 80,110 120,70 160,60 200,80 240,40 280,30 326,10" fill="none" stroke="rgba(255,255,255,.3)" stroke-width="1.5"/></svg>
  </div>
  <div class="plan" style="left:437px;background:var(--green)">
    <div class="plan-name">STANDARD</div><div class="plan-price">300</div><div class="plan-cur">USD</div>
    <svg width="326" height="150" viewBox="0 0 326 150"><polygon points="0,150 0,130 50,115 100,118 150,90 200,70 250,55 290,30 326,5 326,150" fill="rgba(255,255,255,.1)"/><polyline points="0,130 50,115 100,118 150,90 200,70 250,55 290,30 326,5" fill="none" stroke="rgba(255,255,255,.3)" stroke-width="1.5"/></svg>
  </div>
  <div class="plan" style="left:788px;background:var(--cyan)">
    <div class="plan-name">SILVER</div><div class="plan-price">500</div><div class="plan-cur">USD</div>
    <svg width="326" height="150" viewBox="0 0 326 150"><polygon points="0,150 60,120 120,100 180,70 240,50 326,15 326,150" fill="rgba(255,255,255,.12)"/><polyline points="0,150 60,120 120,100 180,70 240,50 326,15" fill="none" stroke="rgba(255,255,255,.3)" stroke-width="1.5"/></svg>
  </div>
</section>

<section class="testimonials" role="img" aria-label="Dimmed photo of people working at laptops">
  <div class="kicker">What people says</div>
  <div class="title">TESTIMONIALS</div>
  <div class="title-rule" style="top:116px"></div>
  <p class="quote">Lorem Ipsum is simply dummy text of the printing and typesetting industry. Lorem Ipsum has been the industry's standard dummy text ever since the 1500s, when an unknown printer took a galley of type and scrambled it to make a type specimen book.</p>
  <svg class="t-arrow" style="left:500px" width="14" height="20" viewBox="0 0 14 20" fill="none" stroke="#fff" stroke-width="2.5"><path d="M11 3 4 10 11 17"/></svg>
  <svg class="t-arrow" style="left:686px" width="14" height="20" viewBox="0 0 14 20" fill="none" stroke="#fff" stroke-width="2.5"><path d="M3 3 10 10 3 17"/></svg>
  <div class="client-name">RENNA CALLOWAY</div>
  <div class="client-role">Client</div>
</section>
<div class="avatar abs" role="img" aria-label="Client portrait" style="background:linear-gradient(135deg,#8a5a44,#d9b49a);border:3px solid #fff"></div>

<section class="news">
  <div class="kicker" style="top:66px">Our blog</div>
  <div class="title" style="top:90px">LATEST NEWS</div>
  <div class="title-rule" style="top:126px"></div>

  <article class="post" style="left:86px">
    <div class="post-image" role="img" aria-label="Diagram of marketing strategy topics" style="background:linear-gradient(135deg,#e8e3d8,#c7b69c)"><div class="post-date">10,November 2016</div></div>
    <h3>Streamlined Marketing Solutions</h3>
    <p>We know the marketing landscape is always changing. We see it everyday in fact. And the only way to thrive amidst change is by being willingto adapt.</p>
    <div class="btn-outline">READ MORE</div>
  </article>
  <article class="post" style="left:437px">
    <div class="post-image" role="img" aria-label="Photo of an open-plan office" style="background:linear-gradient(135deg,#d9dde1,#9aa3ab)"><div class="post-date">11,November 2016</div></div>
    <h3>Streamlined Marketing Solutions</h3>
    <p>We know the marketing landscape is always changing. We see it everyday in fact. And the only way to thrive amidst change is by being willingto adapt.</p>
    <div class="btn-outline">READ MORE</div>
  </article>
  <article class="post" style="left:788px">
    <div class="post-image" role="img" aria-label="Photo of a mood board with printed notes" style="background:linear-gradient(135deg,#e9dfe0,#b55a6e)"><div class="post-date">10,November 2016</div></div>
    <h3>Streamlined Marketing Solutions</h3>
    <p>We know the marketing landscape is always changing. We see it everyday in fact. And the only way to thrive amidst change is by being willingto adapt.</p>
    <div class="btn-outline">READ MORE</div>
  </article>
</section>

<footer class="site-footer">
  <div class="f-col" style="left:86px">
    <h4>CONTACT US</h4>
    <div class="f-item"><span class="f-icon"><svg width="14" height="18" viewBox="0 0 14 18"><path d="M7 1a6 6 0 0 0-6 6c0 4.5 6 10 6 10s6-5.5 6-10a6 6 0 0 0-6-6z" fill="var(--blue)"/><circle cx="7" cy="7" r="2.2" fill="#fff"/></svg></span><span>45 BC, making it over 2000 years<br>Orwell Dene Lane</span></div>
    <div class="f-item"><span class="f-icon"><svg width="16" height="16" viewBox="0 0 16 16"><path d="M3 1h3l1.5 4-2 1.3a8 8 0 0 0 4.2 4.2L11 8.5l4 1.5v3a2 2 0 0 1-2 2C7 15 1 9 1 3a2 2 0 0 1 2-2z" fill="var(--blue)"/></svg></span><span><b>CALL US</b>555-014-2298</span></div>
    <div class="f-item"><span class="f-icon"><svg width="16" height="12" viewBox="0 0 16 12"><rect x="0.5" y="0.5" width="15" height="11" rx="1.5" fill="var(--blue)"/><path d="M1 1.5 8 7l7-5.5" fill="none" stroke="#fff" stroke-width="1.3"/></svg></span><span><b>E-MAIL ADDRESS</b>hello@harbourline.example</span></div>
  </div>
  <div class="f-col f-links" style="left:430px">
    <h4>QUICK LINKS</h4>
    <a href="#">Home</a><a href="#">About</a><a href="#">How We Work</a><a href="#">Learn</a><a href="#">Shop</a><a href="#">Contact</a>
  </div>
  <div class="f-col f-links" style="left:628px">
    <h4>META TAGS</h4>
    <a href="#">Web design</a><a href="#">Content marketing</a><a href="#">Graphic design</a><a href="#">Coaching</a>
  </div>
  <div class="f-col" style="left:845px">
    <h4>NEWSLETTER</h4>
    <div class="field">E-mail address...</div>
    <div class="btn-solid">SUBSCRIBE</div>
  </div>
</footer>

<footer class="bottom-bar">
  <div class="socials"><span class="social"></span><span class="social"></span><span class="social"></span><span class="social"></span></div>
  <div class="copyright">@copyright 2016 Harbourline Studio.All Rights Reserved</div>
</footer>

</body>
</html>
```